Start-up consultancy in Healthcare Space requiring clean and crisp website design

I am the founder of a start-up consultancy to improve access to medicines and healthcare around the globe. My primary product are consulting services to both the public sector and the private sector to work on: improved healthcare delivery, the right price for medicines and addressing challenges in emerging markets. As the sector is fairly conservative, I need a clean and very professional website as is should signal competence in the sector. Therefore, I like shades of white and green but there should be a link to healthcare. Please see the logo that is featured on my business cards.

Target Market(s)

Ministry of Health, Pharmaceutical companies, Emerging Markets (Latin America, Middle East, Eastern Europe, Asia)

Industry/Entity Type

Healthcare

Coding

Coded - Design and coding required

Number of Pages Required

5+ page

Font styles to use
Serif

Colors

Designer to choose colors to be used in the design.

Requirements
Must have
• About Section
• Services Section
• Blog Section
• The website design should also portray the solution for access to healthcare and highlight my ability to help clients with that.
• The website will be hosted on a CMS and should therefore be easy to adjust. I would prefer wordpress but open to any suggestions as I have my own webspace.
• I quite like these websites:
• https://www.tevluma.com/why-tevluma
• https://home.quillfernwell.com/
Nice to have
• I like to see some creative thinking with the theme of healthcare.
Should not have
• The design should not feature too many hospitals or pills etc. as this is really not my focus.

```html
<!DOCTYPE html>
<html lang="en">
<head>
<meta charset="utf-8">
<title>Velmora Consulting</title>
<link href="https://fonts.googleapis.com/css2?family=Lora:wght@400;700&family=Open+Sans:wght@400;600;700&display=swap" rel="stylesheet">
<style>
:root{
  --green-dark:#0b6a38;
  --green-brand:#146b3a;
  --green-icon:#3f6d55;
  --text:#333;
  --muted:#888;
  --light:#f2f2f2;
  --white:#fff;
  --serif:'Lora', Georgia, serif;
  --sans:'Open Sans', Arial, sans-serif;
}
*{margin:0;padding:0;box-sizing:border-box}
html,body{width:1200px;height:2171px;overflow:hidden;background:var(--white)}
body{position:relative;font-family:var(--sans);color:var(--text)}
.abs{position:absolute}

/* header */
.brand{left:132px;top:70px;font-family:var(--serif);font-weight:400;font-size:25px;line-height:32px;color:var(--green-brand);white-space:nowrap}
.sign-in{left:976px;top:33px;width:82px;height:35px;border:1px solid #ccc;font-family:var(--serif);font-size:12px;color:#555;display:flex;align-items:center;justify-content:center;gap:8px}
.nav{left:677px;top:96px;display:flex;gap:26px;font-family:var(--serif);font-size:13px;color:#555;text-transform:uppercase}

/* hero */
.hero{left:0;top:150px;width:1200px;height:464px;background:linear-gradient(100deg,#0da85a 0%,#16c86f 45%,#0aa455 100%)}
.hero-box{left:132px;top:263px;width:320px;height:238px;border:3px solid var(--white);background:rgba(10,100,55,.85);color:var(--white);padding:36px 28px 0 29px}
.hero-box h1{font-family:var(--serif);font-weight:400;font-size:21px;line-height:27px;text-transform:uppercase;margin-bottom:10px}
.hero-box p{font-size:10.5px;line-height:19px}
.hero-arrow{left:439px;top:373px;width:22px;height:22px;border-radius:50%;background:var(--white)}
.dots{left:560px;top:585px;display:flex;gap:17px}
.dots span{width:8px;height:8px;border-radius:50%;background:var(--white)}
.dots span.on{background:transparent;border:1.5px solid var(--white)}

/* intro */
.intro{left:132px;top:688px;width:935px;text-align:center}
.intro h2{font-family:var(--serif);font-weight:400;font-size:22.3px;line-height:31px;color:#444}
.intro p{margin-top:15px;font-size:11px;line-height:19px;color:var(--muted)}

/* services */
.card{top:915px;width:298px;height:415px;background:var(--light);text-align:center}
.card-img{width:100%;height:201px}
.card-icon{position:absolute;left:110px;top:162px;width:78px;height:78px;background:var(--green-icon);border:2px solid var(--white);display:flex;align-items:center;justify-content:center}
.card h3{margin-top:74px;font-family:var(--serif);font-weight:400;font-size:19px;color:var(--green-brand)}
.card p{margin:10px 22px 0;font-size:11px;line-height:17px;color:var(--muted)}
.more{display:inline-block;font-size:11.5px;font-weight:700;text-decoration:underline;color:#222}
.card .more{margin-top:16px}

/* blog */
.blog{left:0;top:1411px;width:1200px;height:400px;background:var(--green-dark);color:var(--white)}
.blog-text{left:132px;top:76px;width:560px}
.blog-text h2{font-family:var(--serif);font-weight:400;font-size:24px}
.blog-text h3{font-family:var(--serif);font-weight:400;font-size:17px;margin-top:13px}
.blog-meta{font-family:var(--serif);font-size:12px;margin-top:17px}
.blog-text p{font-size:11px;line-height:19.5px;margin-top:16px;color:#e6f0ea}
.blog-text .more{color:var(--white);margin-top:20px}
.blog-frame{left:740px;top:80px;width:318px;height:239px;border:3px solid var(--white);padding:13px}
.blog-img{width:100%;height:100%;background:linear-gradient(135deg,#cfeee0,#8fd3b3 60%,#5bb58e)}
.blog-play{left:1047px;top:189px;width:22px;height:22px;border-radius:50%;background:var(--white)}
.chev{top:187px}

/* contact */
.contact{left:0;top:1882px;width:1200px;text-align:center}
.contact h2{font-family:var(--serif);font-weight:400;font-size:23px;color:var(--green-brand)}
.contact p{font-family:var(--serif);font-size:15px;color:var(--muted);margin-top:10px}
.contact-lines{display:flex;justify-content:center;gap:42px;margin-top:22px;font-family:var(--serif);font-size:23px;color:#111}
.contact-lines span{display:flex;align-items:center;gap:10px}

/* footer */
.footer{left:0;top:2074px;width:1200px;height:97px;background:var(--light)}
.footer-links{left:132px;top:27px;font-size:10.5px;color:#666}
.footer-links i{font-style:normal;margin:0 7px}
.copyright{left:132px;top:54px;font-size:10px;color:#777}
.social{left:943px;top:38px;display:flex;gap:8px}
.social span{width:25px;height:25px;border-radius:50%;background:var(--green-icon)}
</style>
</head>
<body>

<header>
  <div class="abs brand">Velmora Consulting</div>
  <div class="abs sign-in">SIGN IN
    <svg width="13" height="13" viewBox="0 0 16 16" fill="none" stroke="#777" stroke-width="1.6"><path d="M9 2h5v12H9M2 8h8M7 5l3 3-3 3"/></svg>
  </div>
  <nav class="abs nav"><span>Home</span><span>About Us</span><span>Services</span><span>Blog</span><span>Contact Us</span></nav>
</header>

<section class="abs hero" role="img" aria-label="Green-toned photo of a doctor writing notes and holding a medicine bottle"></section>
<div class="abs hero-box">
  <h1>Morbi feugiat nibh<br>vitae auctor viverra</h1>
  <p>Cras ut blandit dui. In facilisis erat ac risus consectetur condimentum. Integer vitae nibh pulvinar, egestas libero in, euismod erat. Aenean commodo eros tortor, eget sagittis mi gravida eu. Vestibulum eget orci vitae odio lacinia vestibulum.</p>
</div>
<svg class="abs hero-arrow" viewBox="0 0 22 22"><circle cx="11" cy="11" r="11" fill="#fff"/><path d="M6 11h9M11 7l4 4-4 4" stroke="#0b6a38" stroke-width="2.2" fill="none"/></svg>
<div class="abs dots"><span class="on"></span><span></span><span></span><span></span></div>

<section class="abs intro">
  <h2>Morbi feugiat nibh vitae auctor viverra. Suspendisse potenti. Sed in facilisis quam. Nunc augue felis, mattis at sapien vehicula, semper suscipit nibh.</h2>
  <p>Duis euismod a est non convallis. Donec gravida purus sit amet ex lacinia, et volutpat velit congue. Pellentesque habitant morbi tristique senectus et netus et malesuada fames ac turpis egestas. Duis sed erat scelerisque, mollis ipsum eu, sagittis dolor. Maecenas a semper tellus, vel tempor arcu. Pellentesque convallis dolor tortor, nec iaculis tortor sollicitudin nec. Maecenas faucibus vehicula cursus. Vivamus dictum velit augue, nec porta justo sollicitudin nec. Aliquam at hendrerit dui, imperdiet pharetra velit. Nullam odio lorem, pharetra sed metus id, fermentum porta nibh. Cras fringilla laoreet urna, nec ultricies nulla. Pellentesque vel purus tortor.</p>
</section>

<article class="abs card" style="left:132px">
  <div class="card-img" role="img" aria-label="Photo of a calculator, stethoscope and pen on a billing sheet" style="background:linear-gradient(135deg,#c9d6e6,#8ea6c4)"></div>
  <div class="card-icon"><svg width="36" height="40" viewBox="0 0 36 40" fill="none" stroke="#fff" stroke-width="2"><rect x="5" y="3" width="26" height="34"/><path d="M10 11h3M17 11h9M10 18h3M17 18h9M10 25h3M17 25h9M10 31h3M17 31h9"/></svg></div>
  <h3>Health Plans</h3>
  <p>Maecenas semper tellus, vel tempor arcu. Pellentesque convallis dolor tortor, nec iaculis tortor sollicitudin nec.</p>
  <span class="more">MORE</span>
</article>

<article class="abs card" style="left:452px">
  <div class="card-img" role="img" aria-label="Photo of a hand touching a digital health interface" style="background:linear-gradient(135deg,#e4eef2,#b9d3dc)"></div>
  <div class="card-icon"><svg width="40" height="40" viewBox="0 0 40 40" fill="none" stroke="#fff" stroke-width="3"><circle cx="15" cy="22" r="7"/><path d="M15 11v4M15 29v4M4 22h4M22 22h4M7 14l3 3M20 27l3 3M7 30l3-3M20 17l3-3"/><circle cx="30" cy="10" r="4" stroke-width="2.5"/></svg></div>
  <h3>Health Systems</h3>
  <p>Maecenas semper tellus, vel tempor arcu. Pellentesque convallis dolor tortor, nec iaculis tortor sollicitudin nec.</p>
  <span class="more">MORE</span>
</article>

<article class="abs card" style="left:770px">
  <div class="card-img" role="img" aria-label="Photo of hands holding blister packs of medicine" style="background:linear-gradient(135deg,#eef0f2,#c7cfd6)"></div>
  <div class="card-icon"><svg width="40" height="36" viewBox="0 0 40 36"><path d="M20 3C10 3 3 9 3 16c0 4 2 7 5 9l-2 8 8-5c2 .5 4 .7 6 .7 10 0 17-6 17-13S30 3 20 3z" fill="#fff"/></svg></div>
  <h3>Medical Advices</h3>
  <p>Maecenas semper tellus, vel tempor arcu. Pellentesque convallis dolor tortor, nec iaculis tortor sollicitudin nec.</p>
  <span class="more">MORE</span>
</article>

<section class="abs blog">
  <div class="abs blog-text">
    <h2>Blog</h2>
    <h3>Proin et tempor libero. Vivamus tempus libero ante, non sodales lectus</h3>
    <div class="blog-meta">16 May, 2017 &nbsp;|&nbsp; Mara Linden</div>
    <p>Duis euismod a est non convallis. Donec gravida purus sit amet ex lacinia, et volutpat velit congue. Pellentesque habitant morbi tristique senectus et netus et malesuada fames ac turpis egestas. Duis sed erat scelerisque, mollis ipsum eu, sagittis dolor. Maecenas a semper tellus, vel tempor arcu. Pellentesque convallis dolor tortor, nec iaculis tortor sollicitudin nec. Maecenas faucibus vehicula cursus. Vivamus dictum velit augue, nec porta justo sollicitudin nec. Aliquam at hendrerit dui, imperdiet pharetra velit.</p>
    <span class="more">MORE</span>
  </div>
  <div class="abs blog-frame"><div class="blog-img" role="img" aria-label="Mint-toned photo of a stethoscope and pen on a medical form"></div></div>
  <svg class="abs blog-play" viewBox="0 0 22 22"><circle cx="11" cy="11" r="11" fill="#fff"/><path d="M9 6.5l6 4.5-6 4.5z" fill="#0b6a38"/></svg>
  <svg class="abs chev" style="left:24px" width="14" height="24" viewBox="0 0 14 24"><path d="M12 2L3 12l9 10" stroke="#a9cdb8" stroke-width="2" fill="none"/></svg>
  <svg class="abs chev" style="left:1162px" width="14" height="24" viewBox="0 0 14 24"><path d="M2 2l9 10-9 10" stroke="#a9cdb8" stroke-width="2" fill="none"/></svg>
</section>

<section class="abs contact">
  <h2>Contact Us</h2>
  <p>Quisque scelerisque tempus lacinia. Maecenas vitae vulputate neque.</p>
  <div class="contact-lines">
    <span><svg width="19" height="19" viewBox="0 0 24 24"><path d="M6.6 10.8a15.1 15.1 0 006.6 6.6l2.2-2.2c.3-.3.7-.4 1-.2 1.1.4 2.3.6 3.6.6.6 0 1 .4 1 1V20c0 .6-.4 1-1 1C10.6 21 3 13.4 3 4c0-.6.4-1 1-1h3.5c.6 0 1 .4 1 1 0 1.3.2 2.5.6 3.6.1.3 0 .7-.2 1z" fill="#111"/></svg>555 014 2290</span>
    <span><svg width="21" height="17" viewBox="0 0 24 18"><rect x="1" y="1" width="22" height="16" fill="#111"/><path d="M2 2l10 8 10-8" stroke="#fff" stroke-width="1.8" fill="none"/></svg>info@velmoraconsulting.com</span>
  </div>
</section>

<footer class="abs footer">
  <div class="abs footer-links">Home<i>|</i>About us<i>|</i>Services<i>|</i>Blog<i>|</i>Contact us</div>
  <div class="abs copyright">Copyright &copy; 2017 Velmora Consulting. &nbsp;All rights reserved.</div>
  <div class="abs social" aria-label="Social links"><span></span><span></span><span></span><span></span></div>
</footer>

</body>
</html>
```